Rocket business card

Modern business card design, use of color is good with clean space too.

Things to include on card:

Quote: I add fuel to your optometry practice

- Eyewear Sales
- Admin Duties
- Revenue Collection
- Leadership
- Tech Adoption
- COGS Reduction
- Product Sourcing
-Medical Growth

Dalton Vesk, CEO
Lume Vantor
Text Me! 847-302-6194
dalton@lumevantor.net

```html
<!DOCTYPE html>
<html lang="en">
<head>
<meta charset="UTF-8">
<title>Lume Vantor — Business Card</title>
<link rel="stylesheet" href="https://fonts.googleapis.com/css2?family=Montserrat:wght@400;500;700&display=swap">
<style>
  :root {
    --backdrop: #d9dadc;
    --card-dark: #050505;
    --card-light: #fdfdfd;
    --ink: #1a1a1a;
    --ink-soft: #2b2b2b;
    --white: #ffffff;
    --accent: #ef6a1f;
    --accent-warm: #f5a623;
    --divider: #9a9a9a;
  }
  * { box-sizing: border-box; margin: 0; padding: 0; }
  html, body {
    width: 1200px; height: 800px; overflow: hidden;
    background: var(--backdrop);
    font-family: "Montserrat", Arial, sans-serif;
  }
  .canvas {
    position: relative; width: 1200px; height: 800px;
    display: flex; flex-direction: column; align-items: center; justify-content: center; gap: 40px;
  }
  .card {
    width: 525px; height: 300px; position: relative;
    box-shadow: 0 6px 18px rgba(0,0,0,0.18);
  }

  /* Back side */
  .card-back { background: var(--card-dark); color: var(--white); }
  .tagline {
    position: absolute; top: 34px; left: 0; right: 0; text-align: center;
    font-size: 13px; letter-spacing: 0.08em; font-weight: 500; text-transform: uppercase;
  }
  .tagline .fuel { color: var(--accent-warm); }
  .back-mark {
    position: absolute; top: 84px; left: 0; right: 0;
    display: flex; align-items: center; justify-content: center; gap: 16px;
  }
  .mark-circle {
    width: 74px; height: 74px; border-radius: 50%;
    background: linear-gradient(90deg, var(--accent) 0%, var(--accent-warm) 100%);
  }
  .back-mark .brand-name {
    font-size: 24px; font-weight: 500; letter-spacing: 0.06em; text-transform: uppercase; color: var(--white);
  }
  .services {
    position: absolute; bottom: 34px; left: 0; right: 0; text-align: center;
    font-size: 13px; line-height: 1.55; font-weight: 500;
  }
  .services .dot { color: var(--accent-warm); margin: 0 4px; }

  /* Front side */
  .card-front { background: var(--card-light); color: var(--ink); display: flex; align-items: center; }
  .front-brand {
    width: 255px; display: flex; flex-direction: column; align-items: center; gap: 14px;
  }
  .front-brand .mark-circle { width: 52px; height: 52px; }
  .front-brand .brand-name {
    font-size: 24px; font-weight: 500; letter-spacing: 0.04em; text-transform: uppercase; color: var(--ink);
  }
  .front-divider { width: 1px; height: 120px; background: var(--divider); }
  .contact { padding-left: 36px; }
  .contact-name { color: var(--accent); font-size: 21px; font-weight: 700; letter-spacing: 0.04em; text-transform: uppercase; line-height: 1; }
  .contact-role { font-size: 15px; font-weight: 400; margin-top: 4px; margin-bottom: 16px; letter-spacing: 0.04em; }
  .contact-list { list-style: none; }
  .contact-list li { display: flex; align-items: center; gap: 10px; font-size: 15px; color: var(--ink-soft); line-height: 1.5; }
  .contact-list .phone { font-size: 19px; font-weight: 500; }
  .contact-list svg { width: 14px; height: 14px; flex: none; }
</style>
</head>
<body>
<main class="canvas">

  <section class="card card-back">
    <p class="tagline">I add <span class="fuel">fuel</span> to your optometry practice</p>
    <div class="back-mark">
      <span class="mark-circle"></span>
      <span class="brand-name">Lume Vantor</span>
    </div>
    <p class="services">
      Eyewear Sales<span class="dot">•</span>Admin Duties<span class="dot">•</span>Revenue Collection<span class="dot">•</span>Leadership<br>
      Tech Adoption<span class="dot">•</span>COGS Reduction<span class="dot">•</span>Product Sourcing<span class="dot">•</span>Medical Growth
    </p>
  </section>

  <section class="card card-front">
    <div class="front-brand">
      <span class="mark-circle"></span>
      <span class="brand-name">Lume Vantor</span>
    </div>
    <div class="front-divider"></div>
    <div class="contact">
      <h1 class="contact-name">Dalton Vesk</h1>
      <p class="contact-role">CEO</p>
      <ul class="contact-list">
        <li class="phone">
          <svg viewBox="0 0 24 24" aria-hidden="true"><path fill="#ef6a1f" d="M6.6 10.8a15.1 15.1 0 0 0 6.6 6.6l2.2-2.2c.3-.3.7-.4 1-.2 1.1.4 2.3.6 3.6.6.6 0 1 .4 1 1V20c0 .6-.4 1-1 1A17 17 0 0 1 3 4c0-.6.4-1 1-1h3.5c.6 0 1 .4 1 1 0 1.3.2 2.5.6 3.6.1.3 0 .7-.2 1z"/></svg>
          847-302-6194
        </li>
        <li>
          <svg viewBox="0 0 24 24" aria-hidden="true"><rect x="2.5" y="5" width="19" height="14" fill="none" stroke="#ef6a1f" stroke-width="2"/><path d="M2.5 5l9.5 8 9.5-8M2.5 19l7-6.5M21.5 19l-7-6.5" fill="none" stroke="#ef6a1f" stroke-width="2"/></svg>
          dalton@lumevantor.net
        </li>
        <li>
          <svg viewBox="0 0 24 24" aria-hidden="true"><g fill="none" stroke="#ef6a1f" stroke-width="2"><circle cx="12" cy="12" r="9.5"/><ellipse cx="12" cy="12" rx="4" ry="9.5"/><path d="M2.5 12h19M4 7h16M4 17h16"/></g></svg>
          www.lumevantor.net
        </li>
      </ul>
    </div>
  </section>

</main>
</body>
</html>
```